MARBLED SPARROW WEB DESIGN PROJECT

We are a brand new company called "Marbled Sparrow" which specialise in one-off Vintage Clothing. We would like somebody to design a web page which will be the sole income for our company. Our main aim is to have an easy searchable website which is user friendly. The key to the website is to target people who do not like the idea of op-shopping but love vintage clothes - this website will be the answer.
Updates

This website will need to be coded to work with Tin Lantern - Please read this before you start. https://help.tinlantern.example/articles/Public/How-do-I-create-custom-template-files-for-my-store

Hi everyone, Just want to make note that the this website is for young people. Just so people a clear I want modern young people dressed in Vintage clothes as this is that reality and what they would like to see. Not people dressed like they are going to a fancy dress party, i.e. dresses like it was that era. Thanks Mirela

Coding

Coded - Design and coding required

```html
<!DOCTYPE html>
<html lang="en">
<head>
<meta charset="utf-8">
<title>Marbled Sparrow — Vintage Clothing</title>
<link rel="stylesheet" href="https://fonts.googleapis.com/css2?family=Open+Sans:wght@400;600;700&family=Roboto+Condensed:wght@400;700&family=Raleway:wght@300;400&family=Playfair+Display:ital,wght@0,700;1,400&display=swap">
<style>
:root{
  --blue:#58a9dc;
  --blue-dark:#3f93c8;
  --pink:#eb9a9e;
  --pink-light:#f3b7ba;
  --ink:#333;
  --muted:#777;
  --soft:#999;
  --line:#ddd;
  --page:#f6f6f4;
  --panel:#ececec;
  --star:#f2b705;
  --btn:#555;
  --btn-light:#cfcfcf;
}
*{box-sizing:border-box;margin:0;padding:0}
html,body{width:1200px;height:2913px;overflow:hidden}
body{position:relative;background:var(--page);font-family:"Open Sans",Arial,sans-serif;color:var(--ink);font-size:13px}
.abs{position:absolute}
svg{display:block}

/* top bar */
.topbar{top:0;left:0;width:1200px;height:35px;border-bottom:1px solid var(--line);background:#fff}
.topbar .info{left:100px;top:10px;display:flex;gap:26px;font-size:10px;color:var(--muted);text-transform:uppercase}
.topbar .info span{display:flex;align-items:center;gap:6px}
.topbar .account{right:100px;top:10px;display:flex;font-size:11px;font-weight:600;text-transform:uppercase}
.topbar .account a{color:var(--ink);text-decoration:none;padding:0 11px;border-left:1px solid #999;line-height:12px}
.topbar .account a:first-child{border-left:0}
.topbar .account a:last-child{padding-right:0}

/* header */
.brand{top:48px;left:100px;display:flex;align-items:center;gap:10px}
.brand .mark{width:18px;height:18px;background:var(--blue)}
.brand .name{font-family:"Open Sans",sans-serif;font-size:30px;font-weight:600;color:var(--blue);line-height:1}
.perks{top:64px;left:385px;display:flex;gap:44px}
.perk{display:flex;gap:10px;align-items:center}
.perk b{display:block;font-size:11px;color:var(--ink)}
.perk small{display:block;font-size:10px;color:var(--soft)}
.cart{top:70px;right:100px;display:flex;align-items:center;gap:8px;font-size:11px;color:var(--muted)}

/* nav */
.nav{top:128px;left:0;width:1200px;height:43px;background:var(--blue)}
.nav ul{position:absolute;left:99px;top:0;display:flex;list-style:none;height:43px}
.nav li{color:#fff;font-size:11px;font-weight:600;text-transform:uppercase;padding:0 12px;line-height:43px}
.nav li.active{background:var(--pink);padding:0 19px}
.search{right:100px;top:9px;width:182px;height:25px;background:#fff;border-radius:2px;font-size:11px;color:var(--soft);padding:5px 9px}
.search svg{position:absolute;right:8px;top:7px}

/* hero */
.hero{top:173px;left:0;width:1200px;height:454px;background:linear-gradient(120deg,#e9e9e9 0%,#8a8a8a 30%,#cfcfcf 44%,#6c6c6c 60%,#9a9a9a 80%,#5e5e5e 100%)}
.hero .slogan{left:821px;top:202px;width:329px;height:103px;background:var(--pink);color:#fff;font-family:"Raleway",sans-serif;font-weight:300;font-size:33px;line-height:40px;text-align:center;padding-top:10px}
.hero .arrow{top:200px;width:54px;height:52px;background:#2a2a2a;display:flex;align-items:center;justify-content:center}

/* feature tiles */
.guide{top:654px;left:99px;width:491px;height:342px;background:linear-gradient(180deg,#6d5f58 0%,#8c7a6f 28%,#fff 28%,#fff 60%,#b4564c 60%,#5b7fa4 80%,#8e3f5a 100%)}
.guide .title{position:absolute;left:0;top:110px;width:491px;text-align:center;font-family:"Playfair Display",serif}
.guide .t1{font-size:34px;font-weight:700;letter-spacing:3px;color:#111}
.guide .t1 i{font-weight:400;font-size:38px;letter-spacing:0}
.guide .t2{font-size:44px;font-weight:700;letter-spacing:1px;color:#111;line-height:44px;border-bottom:2px solid #111;display:inline-block}
.guide .t3{font-family:"Open Sans",sans-serif;font-size:17px;letter-spacing:3px;font-weight:600;margin-top:4px}
.arrivals{top:654px;left:612px;width:489px;height:160px;background:var(--pink)}
.arrivals .inner{position:absolute;left:57px;top:29px;width:375px;height:102px;border:1px solid var(--pink-light);display:flex;align-items:center;justify-content:center;gap:12px}
.arrivals .lead{color:#fff;font-family:"Raleway",sans-serif;font-size:27px;line-height:26px}
.arrivals .lead small{display:block;font-size:8px;letter-spacing:2px;color:#fbe1e2;font-family:"Open Sans",sans-serif;margin-top:4px}
.arrivals .off{font-family:"Open Sans",sans-serif;font-weight:700;color:#fff;font-size:44px;letter-spacing:-2px}
.arrivals .off sup{font-size:20px;letter-spacing:0}
.shop-for{top:837px;width:235px;height:159px;color:#fff;font-family:"Raleway",sans-serif;font-size:50px;line-height:48px;text-align:center;padding-top:30px}
.shop-for.men{left:612px;background:linear-gradient(135deg,#6a6a6a,#3c3c3c 55%,#8d8d8d)}
.shop-for.women{left:866px;background:linear-gradient(135deg,#9a9a9a,#4a4a4a 55%,#bdbdbd)}

/* section headings */
.heading{left:99px;width:1002px;border-bottom:2px solid #444;height:34px;display:flex;align-items:flex-end;gap:8px;padding-bottom:4px}
.heading .pin{width:10px;height:36px;background:var(--blue);margin-bottom:-2px}
.heading h2{font-family:"Roboto Condensed",sans-serif;font-weight:700;font-size:26px;color:var(--blue);text-transform:uppercase;line-height:26px}

/* products */
.grid{left:99px;width:1002px;display:grid;grid-template-columns:repeat(4,233px);column-gap:23.3px}
.product{text-align:center}
.product .photo{height:235px;border:1px solid #999}
.product .name{font-size:14px;margin-top:12px;padding-bottom:10px;border-bottom:3px solid var(--pink)}
.product .stars{color:var(--star);font-size:10px;letter-spacing:1px;margin-top:5px;line-height:12px}
.product .price{font-size:15px;font-weight:700;margin-top:15px}
.product .actions{display:flex;justify-content:center;flex-wrap:wrap;gap:6px;width:110px;margin:20px auto 0}
.btn{width:38px;height:38px;border-radius:50%;background:var(--btn);display:flex;align-items:center;justify-content:center}
.btn.light{background:var(--btn-light)}
.btn.accent{background:var(--blue)}
.view-more{left:536px;width:130px;height:37px;border:2px solid #222;background:#fff;display:flex;align-items:center;justify-content:center;gap:12px;font-size:15px}

/* promo row */
.bag-promo{top:1616px;left:99px;width:474px;height:99px;background:var(--panel);display:flex;align-items:center}
.bag-promo .shoppers{width:80px;height:85px;margin-left:20px;background:linear-gradient(160deg,#d8c6b8,#c58f6e 50%,#7a9fc4)}
.bag-promo .copy{margin-left:52px;text-align:center}
.bag-promo .copy b{font-family:"Roboto Condensed",sans-serif;font-size:21px;font-weight:700;color:#222}
.bag-promo .sale{display:flex;align-items:center;justify-content:center;gap:6px;font-size:9px;font-weight:700;color:#222}
.bag-promo .sale strong{font-size:36px;color:#e23b3b;font-family:"Roboto Condensed",sans-serif}
.bag-promo .bag{width:70px;height:70px;margin-left:24px;border-radius:10px;background:linear-gradient(180deg,#e0302e,#a91616)}
.newsletter{top:1616px;left:625px;width:476px;height:99px;background:var(--pink);padding:24px 0 0 25px}
.newsletter h3{font-family:"Roboto Condensed",sans-serif;font-weight:400;font-size:27px;color:#fff;line-height:26px}
.newsletter p{font-size:11px;font-style:italic;color:#f7d3d5}
.newsletter .field{position:absolute;left:200px;top:33px;width:253px;height:28px;background:#fff;font-size:10px;color:var(--soft);padding:7px 8px}
.newsletter .field svg{position:absolute;right:6px;top:5px}

/* tweet band */
.tweets{top:2344px;left:0;width:1200px;height:58px;background:var(--blue)}
.tweets .bird{left:113px;top:14px;width:30px;height:30px;border-radius:50%;background:#fff}
.tweets p{left:160px;top:12px;width:440px;color:#fff;font-size:11px;font-weight:600;line-height:16px}
.tweets .social{right:110px;top:18px;display:flex;gap:10px}
.tweets .social span{width:22px;height:22px;background:#fff;border-radius:2px}

/* footer */
.foot-brand{top:2420px;left:285px;display:flex;align-items:center;gap:10px}
.about-text{top:2505px;left:150px;width:410px;text-align:center;font-size:11px;font-style:italic;color:var(--soft);line-height:15px}
.foot-split{top:2424px;left:608px;width:1px;height:170px;background:var(--line)}
.testimonial{top:2446px;left:640px;width:460px;text-align:center}
.testimonial h4{font-family:"Roboto Condensed",sans-serif;font-size:17px;font-weight:400;color:#444;text-transform:uppercase}
.testimonial .dots{display:flex;justify-content:center;gap:6px;margin:12px 0 10px}
.testimonial .dots i{width:12px;height:12px;border-radius:50%;border:1px solid #bbb;background:#fff}
.testimonial .dots i.on{background:#ccc}
.testimonial p{font-size:11px;color:var(--soft);line-height:15px;width:410px;margin:0 auto}
.foot-rule{top:2598px;left:118px;width:983px;height:1px;background:var(--line)}
.links{top:2633px;left:118px;display:flex}
.links .col{width:167px}
.links h5{font-family:"Roboto Condensed",sans-serif;font-weight:400;font-size:18px;color:#444;text-transform:uppercase;margin-bottom:10px}
.links li{list-style:none;font-size:11px;color:var(--muted);line-height:23.3px}
.links .contact li{display:flex;gap:8px;align-items:flex-start;line-height:15px;margin-bottom:8px}

.bottom{top:2802px;left:0;width:1200px;height:111px;background:#ebebeb;text-align:center}
.payments{display:flex;justify-content:center;gap:32px;margin-top:25px;font-family:"Open Sans",sans-serif;font-weight:700;font-size:13px;color:#9a9a9a}
.bottom .legal{font-size:11px;color:var(--muted);margin-top:14px}
.bottom .legal span{padding:0 8px;border-left:1px solid #aaa}
.bottom .legal span:first-child{border-left:0}
.bottom .copy{font-size:11px;color:var(--muted);margin-top:8px}
</style>
</head>
<body>

<!-- top bar -->
<div class="abs topbar">
  <div class="abs info">
    <span><svg width="10" height="10" viewBox="0 0 10 10"><path d="M2 0h2l1 3-1.5 1a6 6 0 0 0 2.5 2.5L7 5l3 1v2a2 2 0 0 1-2 2A8 8 0 0 1 0 2a2 2 0 0 1 2-2z" fill="#666"/></svg>00-555-010-200</span>
    <span><svg width="10" height="10" viewBox="0 0 10 10"><circle cx="5" cy="5" r="4.3" fill="none" stroke="#666"/><path d="M1 5h8M5 1v8" stroke="#666"/></svg>Language ⌄</span>
    <span><svg width="12" height="9" viewBox="0 0 12 9"><rect x=".5" y=".5" width="11" height="8" fill="none" stroke="#666"/><circle cx="6" cy="4.5" r="2" fill="#666"/></svg>Currency ⌄</span>
  </div>
  <nav class="abs account"><a>My Account</a><a>My Wishlist</a><a>My Cart</a><a>Checkout</a><a>Log In</a></nav>
</div>

<!-- header -->
<div class="abs brand"><span class="mark"></span><span class="name">Marbled Sparrow</span></div>
<div class="abs perks">
  <div class="perk"><svg width="26" height="18" viewBox="0 0 26 18"><rect x="0" y="2" width="16" height="11" fill="#888"/><path d="M17 6h5l3 4v3h-8z" fill="#888"/><circle cx="5" cy="15" r="2.5" fill="#888"/><circle cx="20" cy="15" r="2.5" fill="#888"/></svg><div><b>Free shipping</b><small>Order over $100</small></div></div>
  <div class="perk"><svg width="22" height="20" viewBox="0 0 22 20"><rect x="1" y="6" width="20" height="5" fill="#888"/><rect x="3" y="11" width="16" height="9" fill="#888"/><rect x="10" y="6" width="2" height="14" fill="#fff"/><path d="M11 6C8 0 4 2 7 6M11 6c3-6 7-4 4 0" stroke="#888" stroke-width="2" fill="none"/></svg><div><b>Special weekly</b><small>Offer</small></div></div>
  <div class="perk"><svg width="26" height="16" viewBox="0 0 26 16"><rect x="1" y="1" width="24" height="14" fill="none" stroke="#888" stroke-width="2"/><circle cx="13" cy="8" r="4" fill="#888"/></svg><div><b>Money back</b><small>30 Days</small></div></div>
</div>
<div class="abs cart"><svg width="16" height="15" viewBox="0 0 16 15"><path d="M0 1h3l2 9h9l2-7H4" fill="none" stroke="#999" stroke-width="1.5"/><circle cx="6" cy="13" r="1.5" fill="#999"/><circle cx="13" cy="13" r="1.5" fill="#999"/></svg>Cart: 0 item - $0.00</div>

<!-- navigation -->
<nav class="abs nav">
  <ul><li class="active">Home</li><li>Men</li><li>Women</li><li>Accessories</li><li>Sport</li><li>New Products</li><li>Brands</li><li>Contact Us</li></ul>
  <div class="abs search">Search...<svg width="11" height="11" viewBox="0 0 11 11"><circle cx="4.5" cy="4.5" r="3.5" fill="none" stroke="#888" stroke-width="1.5"/><path d="M7 7l3.5 3.5" stroke="#888" stroke-width="1.5"/></svg></div>
</nav>

<!-- hero -->
<section class="abs hero" role="img" aria-label="Black and white photo of two young women in modern vintage outfits, split diagonally">
  <div class="abs arrow" style="left:0"><svg width="12" height="20" viewBox="0 0 12 20"><path d="M10 2L2 10l8 8" stroke="#fff" stroke-width="2" fill="none"/></svg></div>
  <div class="abs arrow" style="right:0"><svg width="12" height="20" viewBox="0 0 12 20"><path d="M2 2l8 8-8 8" stroke="#fff" stroke-width="2" fill="none"/></svg></div>
  <div class="abs slogan">We love the easy<br>modern elegance</div>
</section>

<!-- feature tiles -->
<section class="abs guide" role="img" aria-label="Brick wall above a rail of colourful vintage garments">
  <div class="title">
    <div class="t1">HOW TO <i>buy</i></div>
    <div class="t2">VINTAGE CLOTHES:</div>
    <div class="t3">9 BEGINNER TIPS</div>
  </div>
</section>
<section class="abs arrivals">
  <div class="inner">
    <div class="lead">NEW ARRIVALS<small>DEALS FROM OUR TOP LABELS</small></div>
    <div class="off">50<sup>%</sup>OFF</div>
  </div>
</section>
<section class="abs shop-for men" role="img" aria-label="Photo of a young man in a dark vintage jacket">For<br>Men</section>
<section class="abs shop-for women" role="img" aria-label="Photo of a young woman in a vintage coat">For<br>Woman</section>

<!-- latest products -->
<div class="abs heading" style="top:1042px"><span class="pin"></span><h2>Latest Products</h2></div>
<div class="abs grid" style="top:1103px">
  <article class="product">
    <div class="photo" role="img" aria-label="Model in white collared top and black skirt" style="background:linear-gradient(180deg,#e8c9d8,#f3e3ea 60%,#c9a9b8)"></div>
    <div class="name">Product 1</div><div class="stars">★★★★★</div><div class="price">$236.99</div>
    <div class="actions">
      <span class="btn light"><svg width="14" height="12" viewBox="0 0 14 12"><path d="M7 12L1 6a3.3 3.3 0 0 1 6-4 3.3 3.3 0 0 1 6 4z" fill="#fff"/></svg></span>
      <span class="btn accent"><svg width="15" height="13" viewBox="0 0 16 15"><path d="M0 1h3l2 9h9l2-7H4" fill="none" stroke="#fff" stroke-width="2"/><circle cx="6" cy="13" r="1.5" fill="#fff"/><circle cx="13" cy="13" r="1.5" fill="#fff"/></svg></span>
      <span class="btn light"><svg width="14" height="14" viewBox="0 0 14 14"><path d="M12 7a5 5 0 1 1-2-4M10 0v3h3" fill="none" stroke="#fff" stroke-width="2"/></svg></span>
      <span class="btn light"><svg width="16" height="10" viewBox="0 0 16 10"><path d="M1 5c4-6 10-6 14 0-4 6-10 6-14 0z" fill="#fff"/><circle cx="8" cy="5" r="2" fill="#cfcfcf"/></svg></span>
    </div>
  </article>
  <article class="product">
    <div class="photo" role="img" aria-label="Model in a brown ruffled vintage dress" style="background:linear-gradient(180deg,#eee,#d8d2ce 40%,#8a6f64 70%,#eee)"></div>
    <div class="name">Product 1</div><div class="stars">★★★★★</div><div class="price">$119.50</div>
    <div class="actions"><span class="btn"><svg width="15" height="13" viewBox="0 0 16 15"><path d="M0 1h3l2 9h9l2-7H4" fill="none" stroke="#fff" stroke-width="2"/><circle cx="6" cy="13" r="1.5" fill="#fff"/><circle cx="13" cy="13" r="1.5" fill="#fff"/></svg></span></div>
  </article>
  <article class="product">
    <div class="photo" role="img" aria-label="Model in a pink fur-trimmed coat" style="background:linear-gradient(180deg,#f2f2f2,#ee7aa8 45%,#e85b94 75%,#f0f0f0)"></div>
    <div class="name">Product 1</div><div class="stars">★★★★★</div><div class="price">$119.50</div>
    <div class="actions"><span class="btn"><svg width="15" height="13" viewBox="0 0 16 15"><path d="M0 1h3l2 9h9l2-7H4" fill="none" stroke="#fff" stroke-width="2"/><circle cx="6" cy="13" r="1.5" fill="#fff"/><circle cx="13" cy="13" r="1.5" fill="#fff"/></svg></span></div>
  </article>
  <article class="product">
    <div class="photo" role="img" aria-label="Model in black beret and white lace blouse" style="background:linear-gradient(180deg,#e7b4cf,#f0e4ea 50%,#3a3a3a 75%,#e5a9c8)"></div>
    <div class="name">Product 1</div><div class="stars">★★★★★</div><div class="price">$1,177.00</div>
    <div class="actions"><span class="btn"><svg width="15" height="13" viewBox="0 0 16 15"><path d="M0 1h3l2 9h9l2-7H4" fill="none" stroke="#fff" stroke-width="2"/><circle cx="6" cy="13" r="1.5" fill="#fff"/><circle cx="13" cy="13" r="1.5" fill="#fff"/></svg></span></div>
  </article>
</div>
<div class="abs view-more" style="top:1550px"><svg width="12" height="8" viewBox="0 0 12 8"><path d="M1 1l5 5 5-5" stroke="#222" stroke-width="1.6" fill="none"/></svg>View More</div>

<!-- promo row -->
<section class="abs bag-promo">
  <div class="shoppers" role="img" aria-label="Illustration of a woman carrying shopping bags"></div>
  <div class="copy"><b>Orvane a beautiful shoulder bag</b><div class="sale">SALE OFF <strong>30%</strong> on weekend</div></div>
  <div class="bag" role="img" aria-label="Red leather shoulder bag"></div>
</section>
<section class="abs newsletter">
  <h3>NEWSLETTER</h3><p>Subscribe To Our Newsletter</p>
  <div class="field">You email here<svg width="16" height="12" viewBox="0 0 16 12"><rect width="16" height="12" fill="#ddd"/><path d="M0 0l8 7 8-7" stroke="#fff" fill="none"/></svg></div>
</section>

<!-- best sale -->
<div class="abs heading" style="top:1755px"><span class="pin"></span><h2>Best Sale</h2></div>
<div class="abs grid" style="top:1816px">
  <article class="product">
    <div class="photo" role="img" aria-label="Model in a floral vintage dress with sunglasses" style="background:linear-gradient(180deg,#dcdcd8,#8e6a64 45%,#6e5a66 80%,#c8c2b8)"></div>
    <div class="name">Product 1</div><div class="stars">★★★★★</div><div class="price">$236.99</div>
    <div class="actions">
      <span class="btn light"><svg width="14" height="12" viewBox="0 0 14 12"><path d="M7 12L1 6a3.3 3.3 0 0 1 6-4 3.3 3.3 0 0 1 6 4z" fill="#fff"/></svg></span>
      <span class="btn accent"><svg width="15" height="13" viewBox="0 0 16 15"><path d="M0 1h3l2 9h9l2-7H4" fill="none" stroke="#fff" stroke-width="2"/><circle cx="6" cy="13" r="1.5" fill="#fff"/><circle cx="13" cy="13" r="1.5" fill="#fff"/></svg></span>
      <span class="btn light"><svg width="14" height="14" viewBox="0 0 14 14"><path d="M12 7a5 5 0 1 1-2-4M10 0v3h3" fill="none" stroke="#fff" stroke-width="2"/></svg></span>
      <span class="btn light"><svg width="16" height="10" viewBox="0 0 16 10"><path d="M1 5c4-6 10-6 14 0-4 6-10 6-14 0z" fill="#fff"/><circle cx="8" cy="5" r="2" fill="#cfcfcf"/></svg></span>
    </div>
  </article>
  <article class="product">
    <div class="photo" role="img" aria-label="Model in polka dot top and bright patterned skirt" style="background:linear-gradient(180deg,#e8e0c8,#f4f4f4 40%,#3e7fa8 65%,#c94a4a 85%,#d8d0b8)"></div>
    <div class="name">Product 1</div><div class="stars">★★★★★</div><div class="price">$119.50</div>
    <div class="actions"><span class="btn"><svg width="15" height="13" viewBox="0 0 16 15"><path d="M0 1h3l2 9h9l2-7H4" fill="none" stroke="#fff" stroke-width="2"/><circle cx="6" cy="13" r="1.5" fill="#fff"/><circle cx="13" cy="13" r="1.5" fill="#fff"/></svg></span></div>
  </article>
  <article class="product">
    <div class="photo" role="img" aria-label="Model in a red hat and dark red patterned dress" style="background:linear-gradient(180deg,#7d8a96,#8c2a30 40%,#5a2228 75%,#6f7a84)"></div>
    <div class="name">Product 1</div><div class="stars">★★★★★</div><div class="price">$119.50</div>
    <div class="actions"><span class="btn"><svg width="15" height="13" viewBox="0 0 16 15"><path d="M0 1h3l2 9h9l2-7H4" fill="none" stroke="#fff" stroke-width="2"/><circle cx="6" cy="13" r="1.5" fill="#fff"/><circle cx="13" cy="13" r="1.5" fill="#fff"/></svg></span></div>
  </article>
  <article class="product">
    <div class="photo" role="img" aria-label="Model in a teal belted vintage dress" style="background:linear-gradient(180deg,#e6e4dc,#2fa38e 40%,#27907c 80%,#d8d6ce)"></div>
    <div class="name">Product 1</div><div class="stars">★★★★★</div><div class="price">$1,177.00</div>
    <div class="actions"><span class="btn"><svg width="15" height="13" viewBox="0 0 16 15"><path d="M0 1h3l2 9h9l2-7H4" fill="none" stroke="#fff" stroke-width="2"/><circle cx="6" cy="13" r="1.5" fill="#fff"/><circle cx="13" cy="13" r="1.5" fill="#fff"/></svg></span></div>
  </article>
</div>
<div class="abs view-more" style="top:2278px"><svg width="12" height="8" viewBox="0 0 12 8"><path d="M1 1l5 5 5-5" stroke="#222" stroke-width="1.6" fill="none"/></svg>View More</div>

<!-- tweet band -->
<section class="abs tweets">
  <span class="abs bird"></span>
  <p class="abs">Dear my friends, We have great news today when Fern Lunar has released, check it out: http://lnk.example/fl33</p>
  <div class="abs social"><span></span><span></span><span></span><span></span><span></span><span></span><span></span><span></span><span></span><span></span><span></span></div>
</section>

<!-- footer -->
<div class="abs foot-brand brand" style="top:2440px;left:290px"><span class="mark"></span><span class="name">Marbled Sparrow</span></div>
<p class="abs about-text">Lorem Ipsum is simply dummy text of the printing and typesetting industry. Lorem Ipsum has been the industry's standard dummy text ever since the when an unknown printer took a galley of type.</p>
<div class="abs foot-split"></div>
<section class="abs testimonial">
  <h4>What clien say ?</h4>
  <div class="dots"><i class="on"></i><i></i><i></i></div>
  <p>Lorem Ipsum is simply dummy text of the printing and typesetting industry. Lorem Ipsum has been the industry's standard dummy text ever since the when an unknown printer took a galley of type.<br>- Hana Ilves -</p>
</section>
<div class="abs foot-rule"></div>

<div class="abs links">
  <div class="col"><h5>Our Offers</h5><ul><li>Delivery</li><li>Service</li><li>Gift Cards</li><li>Mobile</li><li>Manufacturers</li></ul></div>
  <div class="col"><h5>Shipping Info</h5><ul><li>New products</li><li>Top sellers</li><li>Manufactirers</li><li>Suppliers</li><li>Specials</li></ul></div>
  <div class="col"><h5>Our Account</h5><ul><li>My Account</li><li>Orders and Returns</li><li>Site Map</li><li>Search Terms</li><li>Advanced Search</li></ul></div>
  <div class="col"><h5>Informations</h5><ul><li>About Us</li><li>Contact Us</li><li>Customer Service</li><li>Privacy Policy</li><li>Blogs</li></ul></div>
  <div class="col"><h5>Our Account</h5><ul><li>My Account</li><li>Orders and Returns</li><li>Site Map</li><li>Search Terms</li><li>Advanced Search</li></ul></div>
  <div class="col contact"><h5>About Us</h5><ul>
    <li><svg width="9" height="12" viewBox="0 0 9 12"><path d="M4.5 12S0 7 0 4.5a4.5 4.5 0 0 1 9 0C9 7 4.5 12 4.5 12z" fill="#888"/><circle cx="4.5" cy="4.5" r="1.6" fill="#fff"/></svg><span>88 Wren Lane, Suite<br>#12 Ashford, 40210</span></li>
    <li><svg width="10" height="10" viewBox="0 0 10 10"><path d="M2 0h2l1 3-1.5 1a6 6 0 0 0 2.5 2.5L7 5l3 1v2a2 2 0 0 1-2 2A8 8 0 0 1 0 2a2 2 0 0 1 2-2z" fill="#888"/></svg><span>+00 555 010 789</span></li>
    <li><svg width="11" height="9" viewBox="0 0 11 9"><rect width="11" height="9" fill="#888"/><path d="M0 0l5.5 5L11 0" stroke="#fff" fill="none"/></svg><span>hello@ferntheme.example</span></li>
  </ul></div>
</div>

<footer class="abs bottom">
  <div class="payments"><span>Cardnova</span><span>Orbpay</span><span>Paywell</span><span>Swiftly</span></div>
  <div class="legal"><span>About Us</span><span>Customer Service</span><span>Privacy Policy</span></div>
  <div class="copy">© 2014 Tin Lantern Demo Store. All Rights Reserved. Designed by <b>FernTheme.example</b></div>
</footer>

</body>
</html>
```